Parfume Label

Hi
We are searching a design-label for our new parfume that we will launch soon.
The Brand of the company is http://www.marek-vossun.ch/.
Please be aware that the label will be screen printed on a glass bottle.
The name of the parfume will be: Sea Glow
So for us its important that the name Sea Glow should be prominent on the label and the brand MAREK VOSSUN only small to get the relation to the brand. To have same CI the name MAREK VOSSUN should be written with our special font that i have attached. It also not necessary to put the MAREK VOSSUN on a black background because with the screen print it will not look good.
For the Sea Glow you can use what ever you like, feel free to design.
In advance thanks for all designers that participate.
Have fun...

```html
<!DOCTYPE html>
<html lang="en">
<head>
<meta charset="utf-8">
<title>Marek Vossun – Sea Glow Label</title>
<link rel="stylesheet" href="https://fonts.googleapis.com/css2?family=Barlow+Semi+Condensed:wght@700&family=Marcellus+SC&display=swap">
<style>
  :root {
    --paper: #ffffff;
    --ink: #000000;
    --label-rose: #dd8483;
    --label-text: #ffffff;
    --frame: #1a1a1a;
    --glass-light: #fbfbfb;
    --glass-mid: #e4e4e6;
    --glass-edge: #c9c9cc;
    --scent-amber: #eadcb8;
  }
  * { box-sizing: border-box; margin: 0; padding: 0; }
  html, body {
    width: 1200px;
    height: 748px;
    overflow: hidden;
    background: var(--paper);
  }
  .board {
    position: relative;
    width: 1200px;
    height: 748px;
    background: var(--paper);
    border: 1px solid var(--frame);
    overflow: hidden;
  }
  .brand-band {
    position: absolute;
    left: 0;
    top: 9px;
    width: 506px;
    height: 75px;
    background: var(--ink);
    color: var(--label-text);
    font-family: "Barlow Semi Condensed", "Arial Narrow", sans-serif;
    font-weight: 700;
    font-size: 44px;
    letter-spacing: 0.5px;
    display: flex;
    align-items: center;
    justify-content: flex-end;
    padding-right: 16px;
    padding-top: 4px;
  }

  /* Product photography areas */
  .bottle {
    position: absolute;
  }
  .bottle--round {
    left: 235px;
    top: 131px;
    width: 308px;
    height: 468px;
    border-radius: 150px 150px 140px 140px;
    background: radial-gradient(ellipse at 50% 60%, var(--glass-light) 45%, var(--glass-mid) 80%, var(--glass-edge) 100%);
  }
  .bottle--square {
    left: 675px;
    top: 164px;
    width: 287px;
    height: 470px;
    border-radius: 18px;
    background: linear-gradient(180deg, var(--glass-mid) 0%, var(--glass-light) 30%, var(--scent-amber) 60%, var(--glass-mid) 85%, var(--paper) 100%);
  }

  .label {
    position: absolute;
    background: var(--label-rose);
  }
  .label--round {
    left: 281px;
    top: 334px;
    width: 218px;
    height: 218px;
    border-radius: 50%;
  }
  .label--square {
    left: 728px;
    top: 383px;
    width: 185px;
    height: 120px;
  }
  .label__brand {
    position: absolute;
    background: var(--ink);
    color: var(--label-text);
    font-family: "Barlow Semi Condensed", "Arial Narrow", sans-serif;
    font-weight: 700;
    font-size: 18px;
    letter-spacing: 0.3px;
    display: flex;
    align-items: center;
    justify-content: center;
    white-space: nowrap;
  }
  .label--round .label__brand {
    left: 6px;
    top: 38px;
    width: 169px;
    height: 27px;
  }
  .label--square .label__brand {
    left: 0;
    top: 14px;
    width: 173px;
    height: 26px;
  }
  .label__name {
    position: absolute;
    left: 0;
    right: 0;
    text-align: center;
    color: var(--label-text);
    font-family: "Marcellus SC", "Times New Roman", serif;
    font-weight: 400;
    font-size: 40px;
    line-height: 1;
    white-space: nowrap;
  }
  .label--round .label__name { top: 92px; }
  .label--square .label__name { top: 56px; font-size: 34px; }
</style>
</head>
<body>
  <main class="board">
    <header class="brand-band">MAREK VOSSUN</header>

    <div class="bottle bottle--round" role="img" aria-label="Photo of a round clear glass perfume bottle with a disc stopper"></div>
    <div class="bottle bottle--square" role="img" aria-label="Photo of a square glass perfume bottle with amber scent and clear cap"></div>

    <section class="label label--round" aria-label="Round bottle label">
      <div class="label__brand">MAREK VOSSUN</div>
      <h1 class="label__name">Sea Glow</h1>
    </section>

    <section class="label label--square" aria-label="Square bottle label">
      <div class="label__brand">MAREK VOSSUN</div>
      <h2 class="label__name">Sea Glow</h2>
    </section>
  </main>
</body>
</html>
```